Professional DJ Business Card

Business card for giving out to clubs and venues or interested groups that are in need of a professional DJ. I want something artistic and catchy/alluring, with a minimalist approach that gets just the vital amount of info and leaves the rest for inquiry via contacting me. Ideally I would like one side to have an image of something cool like an eye and my name, then the other side be the contact info, I am definitely feeling a black or dark colored card, but I am open to other designs. I am uploading a picture that I made that reflects a little of what I am *kind of* looking for.

Industry/Entity Type

Business

Contact Information for Business Card

Tomas Halvik (Voxtel)
Professional DJ (West Coast)
EDM (Deep/House/Techno), Hip Hop, Latin, Trap.
Cell: 555-274-9163
Email: Voxtelofficial@mailnest.net
www.beatcloudia.net/yourtuneisfading

```html
<!DOCTYPE html>
<html lang="en">
<head>
<meta charset="utf-8">
<title>Tomas Halvik (Voxtel) – DJ Business Card</title>
<link rel="stylesheet" href="https://fonts.googleapis.com/css2?family=Archivo:wght@500;700&display=swap">
<style>
  :root {
    --card-bg: #080808;
    --ink: #ffffff;
    --font-main: "Archivo", "Helvetica Neue", Arial, sans-serif;
  }
  html, body {
    margin: 0;
    padding: 0;
    width: 1200px;
    height: 702px;
    overflow: hidden;
    background: var(--card-bg);
  }
  .card {
    position: relative;
    width: 1200px;
    height: 702px;
    background: var(--card-bg);
    color: var(--ink);
    font-family: var(--font-main);
    overflow: hidden;
  }
  .brand-mark {
    position: absolute;
    left: 202px;
    top: 253px;
    width: 120px;
    height: 120px;
  }
  .brand-name {
    position: absolute;
    left: 162px;
    width: 200px;
    top: 448px;
    margin: 0;
    text-align: center;
    font-size: 27px;
    font-weight: 500;
    letter-spacing: 0.62em;
    padding-left: 0.62em;
    line-height: 1;
  }
  .details {
    position: absolute;
    left: 515px;
    top: 0;
    margin: 0;
    text-transform: uppercase;
  }
  .details p { margin: 0; position: absolute; left: 0; white-space: nowrap; line-height: 1; }
  .holder-name { top: 153px; font-size: 41px; font-weight: 700; letter-spacing: 0.01em; }
  .holder-role { top: 200px; font-size: 29px; font-weight: 500; letter-spacing: 0.02em; }
  .genres-edm { top: 275px; font-size: 29px; font-weight: 500; letter-spacing: 0.02em; }
  .genres-other { top: 313px; font-size: 29px; font-weight: 500; letter-spacing: 0.02em; }
  .phone { top: 395px; font-size: 39px; font-weight: 700; letter-spacing: 0.01em; }
  .email, .website {
    text-transform: none;
    font-size: 29px;
    font-weight: 500;
    letter-spacing: 0.01em;
  }
  .email { top: 478px; }
  .website { top: 516px; }
</style>
</head>
<body>
  <main class="card">
    <svg class="brand-mark" viewBox="0 0 120 120" aria-hidden="true">
      <circle cx="60" cy="60" r="55" fill="none" stroke="var(--ink)" stroke-width="7"/>
    </svg>
    <p class="brand-name">VOXTEL</p>

    <section class="details">
      <p class="holder-name">Tomas Halvik (Voxtel)</p>
      <p class="holder-role">Professional DJ (West Coast)</p>
      <p class="genres-edm">EDM (Deep/House/Techno)</p>
      <p class="genres-other">Hip Hop, Latin, Trap</p>
      <p class="phone">555-274-9163</p>
      <p class="email">Voxtelofficial@mailnest.net</p>
      <p class="website">www.beatcloudia.net/yourtuneisfading</p>
    </section>
  </main>
</body>
</html>
```